letterhead design

We have a business card with logo, ink etc and want to develop letterhead that uses the elements of the business card logo.
Must haves...and they should be designed in, not just plopped in :)
Dr. Lyle Varden
2817 W Marlow Street
Fresno, CA 93614
559-382-6157 p
559-382-7043 f
info@brindlespine.com
www.brindlespine.com
www.facebook.com/brindlespn
Updates

Rather than just have the logo on the page, is there someway to silkscreen it in the background to fill the page?

Reason: I was out of town for a week.

Industry/Entity Type

Business

Requirements
Nice to have
• I'd like the logo somehow silk screened in the background of the paper as well.

```html
<!DOCTYPE html>
<html lang="en">
<head>
<meta charset="utf-8">
<title>Brindle Spine Letterhead</title>
<link href="https://fonts.googleapis.com/css2?family=Arimo:wght@400;700&family=Cormorant+Garamond:ital,wght@1,500&family=Italianno&display=swap" rel="stylesheet">
<style>
  :root {
    --brown: #7a4138;
    --tan: #e8c794;
    --emblem-light: #d9ab6e;
    --emblem-dark: #b98246;
    --cream: #fff8ee;
    --paper: #ffffff;
    --ghost: #e3e3e3;
  }
  html, body {
    margin: 0;
    padding: 0;
    overflow: hidden;
    background: var(--paper);
  }
  .letterhead {
    position: relative;
    width: 912px;
    height: 1200px;
    overflow: hidden;
    background: var(--paper);
    font-family: "Arimo", Arial, sans-serif;
  }
  .header-band {
    position: absolute;
    left: 0;
    top: 0;
    width: 912px;
    height: 372px;
  }
  .web-links {
    position: absolute;
    right: 16px;
    top: 2px;
    text-align: right;
    font-family: "Cormorant Garamond", Georgia, serif;
    font-style: italic;
    font-weight: 500;
    font-size: 19px;
    line-height: 27px;
    color: var(--cream);
  }
  .doctor-name {
    position: absolute;
    left: 290px;
    top: 66px;
    margin: 0;
    font-family: "Italianno", cursive;
    font-weight: 400;
    font-size: 76px;
    line-height: 1;
    color: var(--cream);
  }
  .address {
    position: absolute;
    left: 505px;
    top: 158px;
    font-size: 20px;
    line-height: 30px;
    color: var(--cream);
    text-align: center;
  }
  .contact {
    position: absolute;
    left: 2px;
    top: 220px;
    color: var(--cream);
  }
  .contact-title {
    display: block;
    margin-left: 85px;
    font-size: 14px;
    line-height: 20px;
  }
  .contact-line {
    display: block;
    margin-left: 44px;
    font-size: 18.5px;
    line-height: 24px;
  }
  .contact-email {
    display: block;
    font-size: 17px;
    line-height: 26px;
    margin-top: 2px;
  }
  .emblem-panel {
    position: absolute;
    left: 713px;
    top: 73px;
    width: 199px;
    height: 240px;
    background: linear-gradient(135deg, var(--emblem-light), var(--emblem-dark));
  }
  .ghost-mark {
    position: absolute;
    left: 0;
    top: 630px;
    width: 912px;
    text-align: center;
    font-family: "Arimo", Arial, sans-serif;
    font-weight: 700;
    font-size: 112px;
    line-height: 1;
    color: var(--ghost);
  }
</style>
</head>
<body>
<main class="letterhead">
  <svg class="header-band" viewBox="0 0 912 372" aria-hidden="true">
    <rect x="0" y="0" width="912" height="320" fill="var(--brown)"/>
    <path d="M0 180 C 120 120, 260 50, 420 46 C 600 40, 760 58, 912 60
             L 912 372 C 870 360, 800 330, 740 300
             C 600 245, 470 215, 330 195 C 200 180, 90 190, 0 215 Z"
          fill="var(--tan)"/>
  </svg>

  <div class="web-links">
    <div>www.brindlespine.com</div>
    <div>www.facebook.com/brindlespn</div>
  </div>

  <h1 class="doctor-name">Dr. Lyle Varden</h1>

  <div class="address">
    <div>2817 W Marlow Street</div>
    <div>Fresno, CA 93614</div>
  </div>

  <div class="emblem-panel" role="img" aria-label="Chiropractic health emblem artwork"></div>

  <div class="contact">
    <span class="contact-title">CONTACT US :</span>
    <span class="contact-line">559-382-6157 p</span>
    <span class="contact-line">559-382-7043 f</span>
    <span class="contact-email">info@brindlespine.com</span>
  </div>

  <div class="ghost-mark">Brindle Spine</div>
</main>
</body>
</html>
```